Criação de Manual da Marca para Marketing & Comunicação
A empresa queria:
" Vamos iniciar atividade em junho. Incialmente, eugência com prestadores terceirizados, venda via network, em seguida tráfego pago e orgânico. Pretendo terceirizar a produção de criativos e vídeos. "

```html
<!DOCTYPE html>
<html lang="pt-BR">
<head>
<meta charset="UTF-8">
<title>Manual da Marca — Novaforma</title>
<link rel="stylesheet" href="https://fonts.googleapis.com/css2?family=Montserrat:ital,wght@0,400;0,600;0,700;1,400&display=swap">
<style>
  :root {
    --canvas-bg: #ffffff;
    --page-light: #d6d4d2;
    --page-mid: #c6c4c2;
    --page-dark: #aeacaa;
    --ink: #1c1c1c;
    --ink-soft: #2e2e2e;
    --accent-gray: #7d7d7d;
    --accent-pink: #e07fb0;
    --accent-blue: #7cc4e8;
    --accent-yellow: #f1e88a;
  }
  * { margin: 0; padding: 0; box-sizing: border-box; }
  html, body {
    width: 1200px;
    height: 1200px;
    overflow: hidden;
    background: var(--canvas-bg);
    font-family: "Montserrat", sans-serif;
  }
  .spread {
    position: absolute;
    left: 0;
    top: 228px;
    width: 1200px;
    height: 744px;
    background: radial-gradient(ellipse 70% 90% at 62% 45%, var(--page-light) 0%, var(--page-mid) 55%, var(--page-dark) 100%);
    overflow: hidden;
  }
  .brand-decoration {
    position: absolute;
    left: 0;
    top: 70px;
    width: 480px;
    height: 590px;
    border-radius: 0 28px 28px 0;
    background: linear-gradient(150deg,
      rgba(125,125,125,0.18) 0%,
      rgba(224,127,176,0.14) 40%,
      rgba(124,196,232,0.14) 65%,
      rgba(241,232,138,0.18) 100%);
  }
  .brand-signature {
    position: absolute;
    left: 520px;
    top: 520px;
    display: flex;
    align-items: center;
    gap: 12px;
  }
  .brand-signature .mark-square {
    width: 26px;
    height: 26px;
    border: 3px solid var(--ink-soft);
    border-radius: 4px;
  }
  .brand-signature .brand-name {
    font-weight: 600;
    font-size: 28px;
    letter-spacing: 2px;
    color: var(--ink-soft);
  }
  .manual-intro {
    position: absolute;
    left: 943px;
    top: 206px;
    width: 232px;
    color: var(--ink);
  }
  .manual-intro h2 {
    font-weight: 700;
    font-size: 17px;
    margin-bottom: 8px;
  }
  .manual-intro p {
    font-size: 10.5px;
    line-height: 1.75;
    text-align: justify;
    margin-bottom: 14px;
  }
  .manual-intro em { font-style: italic; }
  .manual-intro strong { font-weight: 700; }
  .page-number {
    position: absolute;
    right: 22px;
    bottom: 88px;
    font-size: 9px;
    font-weight: 600;
    color: var(--ink-soft);
  }
</style>
</head>
<body>
  <section class="spread">
    <div class="brand-decoration" role="img" aria-label="Elemento decorativo da marca em tons de cinza, rosa, azul e amarelo"></div>

    <div class="brand-signature">
      <span class="mark-square"></span>
      <span class="brand-name">NOVAFORMA</span>
    </div>

    <article class="manual-intro">
      <h2>O que é o manual?</h2>
      <p><em>Manual</em> é a publicação das normas técnicas que regem a aplicação e replicação da marca. Ele é um guia para sua comunicação visual. Quanto mais de acordo os materiais estiverem com as regras descritas neste manual, mais eficiente será a comunicação da empresa.</p>
      <p>Consulte-o sempre que for preciso e contribua para a solidez e valorização da marca <strong>NOVAFORMA.</strong></p>
    </article>

    <span class="page-number">03</span>
  </section>
</body>
</html>
```